Business Card design which attached logo. Company is called Tailored Shield and main colours are Orange & Black.

Company specialises in Paint Protection and Detailing for supercars.

Details needed on business card:

Sales

Address: Unit 14, 227 Harlow Street, Fernmere Vale, NSW 2391

Phone: 02 8419 2753

website: www.tailoredshield.com.au

Email: sales@tailoredshield.com.au

```html
<!DOCTYPE html>
<html lang="en">
<head>
<meta charset="utf-8">
<title>Tailored Shield – Business Card</title>
<link href="https://fonts.googleapis.com/css2?family=Montserrat:wght@300;400&display=swap" rel="stylesheet">
<style>
  :root {
    --backdrop: #1c1d20;
    --card: #0b0b0c;
    --card-edge: #151517;
    --orange: #e3561f;
    --text: #c4c4c4;
  }
  html, body {
    margin: 0;
    padding: 0;
    width: 1200px;
    height: 900px;
    overflow: hidden;
    background: var(--backdrop);
    font-family: "Montserrat", Arial, sans-serif;
  }
  .canvas {
    position: relative;
    width: 1200px;
    height: 900px;
  }
  .card {
    position: absolute;
    width: 620px;
    height: 354px;
    background: var(--card);
    border: 1px solid var(--card-edge);
    box-sizing: border-box;
    overflow: hidden;
  }
  .card--front { left: 150px; top: 70px; }
  .card--back  { left: 430px; top: 476px; }

  /* front */
  .brand {
    position: absolute;
    left: 250px;
    top: 64px;
    margin: 0;
    color: var(--orange);
    font-weight: 300;
    font-size: 26px;
    letter-spacing: 1px;
    text-transform: uppercase;
  }
  .rule {
    position: absolute;
    height: 1.5px;
    background: var(--orange);
  }
  .rule--top    { left: 60px; top: 124px; width: 500px; }
  .rule--bottom { left: 40px; top: 306px; width: 480px; }
  .person {
    position: absolute;
    left: 290px;
    top: 140px;
    margin: 0;
    color: var(--orange);
    font-weight: 300;
    font-size: 21px;
    letter-spacing: 1px;
    text-transform: uppercase;
  }
  .contact {
    position: absolute;
    left: 60px;
    margin: 0;
    display: flex;
    align-items: center;
    gap: 9px;
    color: var(--text);
    font-weight: 300;
    font-size: 15px;
  }
  .contact--phone-mail { top: 188px; }
  .contact--web        { top: 226px; left: 110px; }
  .contact--address    { top: 262px; left: 40px; }
  .contact svg { width: 14px; height: 14px; flex: none; }
  .divider {
    width: 2px;
    height: 16px;
    background: var(--orange);
    margin: 0 10px 0 14px;
  }

  /* back */
  .back-mark {
    position: absolute;
    inset: 0;
    display: flex;
    align-items: center;
    justify-content: center;
    gap: 10px;
  }
  .back-dot {
    width: 16px;
    height: 16px;
    border: 1.5px solid var(--orange);
    border-radius: 50%;
  }
  .back-name {
    color: var(--orange);
    font-weight: 300;
    font-size: 16px;
    letter-spacing: 1px;
    text-transform: uppercase;
  }
</style>
</head>
<body>
<main class="canvas">

  <section class="card card--front">
    <h1 class="brand">Tailored Shield</h1>
    <div class="rule rule--top"></div>
    <h2 class="person">Daniel Reyes</h2>

    <p class="contact contact--phone-mail">
      <svg viewBox="0 0 24 24" aria-hidden="true"><path fill="#e3561f" d="M6.6 10.8a15 15 0 0 0 6.6 6.6l2.2-2.2a1 1 0 0 1 1-.25 11.4 11.4 0 0 0 3.6.57 1 1 0 0 1 1 1V20a1 1 0 0 1-1 1A17 17 0 0 1 3 4a1 1 0 0 1 1-1h3.5a1 1 0 0 1 1 1c0 1.25.2 2.45.57 3.6a1 1 0 0 1-.25 1z"/></svg>
      <span>02 8419 2753</span>
      <span class="divider"></span>
      <svg viewBox="0 0 24 24" aria-hidden="true"><rect x="2" y="5" width="20" height="14" fill="#e3561f"/><path d="M2 5l10 8 10-8" fill="none" stroke="#0b0b0c" stroke-width="2"/></svg>
      <span>sales@tailoredshield.com.au</span>
    </p>

    <p class="contact contact--web">
      <svg viewBox="0 0 24 24" aria-hidden="true"><circle cx="12" cy="12" r="10" fill="#e3561f"/><path d="M2 12h20M12 2c3 3 3 17 0 20M12 2c-3 3-3 17 0 20" fill="none" stroke="#0b0b0c" stroke-width="1.5"/></svg>
      <span>www.tailoredshield.com.au</span>
    </p>

    <p class="contact contact--address">
      <span>Unit 14, 227 Harlow Street, Fernmere Vale, NSW 2391</span>
    </p>

    <div class="rule rule--bottom"></div>
  </section>

  <section class="card card--back">
    <div class="back-mark">
      <span class="back-dot"></span>
      <span class="back-name">Tailored Shield</span>
    </div>
  </section>

</main>
</body>
</html>
```